KVO-Business Card Design

I need a modern, professional business card design that includes my logo as the main feature, maybe the entire background with the contact info overlaying or even contact info on the back and the logo full frontal

Neat and organized placement of contact information

Would like to see options in black and white

Target Market(s)

real estate Developers, Construction managers, business and home owners

Industry/Entity Type

Construction

Contact Information for Business Card

KVO Construction
Danny Ferrante
General Contractor

Office: 1-888-902-7315 Ext #1
Cell: 215-730-4162
Fax: 1-888-902-7315

Font styles to use
Serif

Requirements
Must have
• title
• office #
• cell #
• Email
• website
Nice to have
• fax

```html
<!DOCTYPE html>
<html lang="en">
<head>
<meta charset="utf-8">
<title>KVO Construction – Business Card</title>
<link rel="stylesheet" href="https://fonts.googleapis.com/css2?family=Saira+Condensed:wght@400;500;700&display=swap">
<style>
  :root {
    --page-bg: #e6e4e0;
    --card-black: #060606;
    --brand-green: #5fb32e;
    --brand-green-deep: #1f8a36;
    --text-light: #f4f4f4;
    --back-tint: #dcefc4;
    --back-white: #ffffff;
  }
  * { margin: 0; padding: 0; box-sizing: border-box; }
  html, body {
    width: 1200px; height: 1200px; overflow: hidden;
    background: var(--page-bg);
    font-family: "Saira Condensed", sans-serif;
  }
  .canvas {
    width: 1200px; height: 1200px;
    display: flex; flex-direction: column; align-items: center; justify-content: center;
    gap: 40px;
  }
  .card {
    width: 940px; height: 537px; position: relative;
    box-shadow: 0 6px 18px rgba(0,0,0,0.18);
  }

  /* Back side: brand */
  .card-back {
    background: radial-gradient(ellipse at center, var(--back-white) 35%, var(--back-tint) 100%);
    display: flex; flex-direction: column; align-items: center; justify-content: center;
    gap: 14px;
  }
  .brand-name {
    display: flex; align-items: center; gap: 18px;
    color: var(--brand-green-deep); font-weight: 700; font-size: 84px; line-height: 1;
    letter-spacing: 1px;
  }
  .brand-mark {
    width: 44px; height: 44px; border-radius: 50%;
    background: var(--brand-green-deep); flex: none;
  }
  .back-web {
    color: var(--brand-green-deep); font-size: 26px; letter-spacing: 6px;
  }

  /* Front side: contact */
  .card-front {
    background: var(--card-black);
    display: flex; align-items: center;
  }
  .front-brand {
    width: 50%; display: flex; justify-content: center; align-items: center;
  }
  .front-brand .brand-name { color: var(--brand-green); font-size: 64px; gap: 14px; }
  .front-brand .brand-mark { width: 34px; height: 34px; background: var(--brand-green); }

  .contact {
    width: 50%; display: flex; flex-direction: column; gap: 44px;
    padding-right: 40px;
  }
  .contact-group {
    border-left: 2px solid var(--brand-green-deep);
    padding-left: 18px; display: flex; flex-direction: column; gap: 10px;
  }
  .person-name {
    color: var(--brand-green); font-weight: 700; font-size: 46px; line-height: 1;
    letter-spacing: 0.5px;
  }
  .person-title { color: var(--text-light); font-size: 30px; line-height: 1.1; }
  .contact-line {
    display: flex; align-items: center; gap: 12px;
    color: var(--text-light); font-size: 30px; line-height: 1.1;
  }
  .contact-icon { width: 24px; height: 24px; flex: none; }
</style>
</head>
<body>
<main class="canvas">

  <section class="card card-back" aria-label="Business card back">
    <div class="brand-name"><span class="brand-mark"></span>KVO Construction</div>
    <div class="back-web">www.kvoconstruction.com</div>
  </section>

  <section class="card card-front" aria-label="Business card front">
    <div class="front-brand">
      <div class="brand-name"><span class="brand-mark"></span>KVO Construction</div>
    </div>

    <div class="contact">
      <div class="contact-group">
        <div class="person-name">DANNY FERRANTE</div>
        <div class="person-title">General Contractor</div>
        <div class="contact-line">
          <svg class="contact-icon" viewBox="0 0 24 24" aria-label="Cell">
            <circle cx="12" cy="12" r="12" fill="#1f8a36"/>
            <rect x="9" y="5" width="6" height="14" rx="1.2" fill="none" stroke="#fff" stroke-width="1.6"/>
            <circle cx="12" cy="16.5" r="0.9" fill="#fff"/>
          </svg>215-730-4162
        </div>
      </div>

      <div class="contact-group">
        <div class="contact-line">
          <svg class="contact-icon" viewBox="0 0 24 24" aria-label="Fax">
            <circle cx="12" cy="12" r="12" fill="#1f8a36"/>
            <rect x="8" y="5.5" width="8" height="5" fill="none" stroke="#fff" stroke-width="1.4"/>
            <rect x="5.5" y="10.5" width="13" height="7" rx="1" fill="#fff"/>
          </svg>1-888-902-7315
        </div>
        <div class="contact-line">
          <svg class="contact-icon" viewBox="0 0 24 24" aria-label="Office">
            <circle cx="12" cy="12" r="12" fill="#1f8a36"/>
            <path d="M5 10 Q12 5 19 10 L17 12 L15 10.5 L9 10.5 L7 12 Z" fill="#fff"/>
            <rect x="7" y="12" width="10" height="6" rx="1" fill="#fff"/>
          </svg>1-888-902-7315 Ext #1
        </div>
      </div>

      <div class="contact-group">
        <div class="contact-line">
          <svg class="contact-icon" viewBox="0 0 24 24" aria-label="Website">
            <circle cx="12" cy="12" r="12" fill="#1f8a36"/>
            <circle cx="12" cy="12" r="6.5" fill="none" stroke="#fff" stroke-width="1.4"/>
            <ellipse cx="12" cy="12" rx="3" ry="6.5" fill="none" stroke="#fff" stroke-width="1.2"/>
            <line x1="5.5" y1="12" x2="18.5" y2="12" stroke="#fff" stroke-width="1.2"/>
          </svg>www.kvoconstruction.com
        </div>
        <div class="contact-line">
          <svg class="contact-icon" viewBox="0 0 24 24" aria-label="Email">
            <circle cx="12" cy="12" r="12" fill="#1f8a36"/>
            <rect x="6" y="8" width="12" height="8" rx="1" fill="#fff"/>
            <path d="M6 8 L12 13 L18 8" fill="none" stroke="#1f8a36" stroke-width="1.2"/>
          </svg>danny@kvoconstruction.com
        </div>
      </div>
    </div>
  </section>

</main>
</body>
</html>
```